ticket wallet design

We are a travel agent, need a design for our PVC resealable ticket wallet - size 27cm X 17.5cm. would like the design be colorful , delightful and looking forward to their trip. need our logo on it as well, logo size and color can be vary.
prefer simple design, not too complicated
Updates

Designs look the same

Requirements
Nice to have
• world landmarks or photos...
• OR the whole design stays simple colorful and delightful.
Should not have

```html
<!DOCTYPE html>
<html lang="ja">
<head>
<meta charset="utf-8">
<title>Skybridge Travel — Japan Ticket Wallet</title>
<link rel="stylesheet" href="https://fonts.googleapis.com/css2?family=Noto+Sans+JP:wght@300;400;500&family=Montserrat:wght@600&display=swap">
<style>
  :root {
    --sky: #27a8e2;
    --mid-blue: #3b82cf;
    --violet: #5b4cab;
    --purple: #673a9e;
    --white: #ffffff;
    --cream: #f4ecd8;
    --ink: #121214;
    --silhouette: 62, 58, 60;
  }
  html, body {
    margin: 0;
    padding: 0;
    overflow: hidden;
    background: #e9ecef;
  }
  .wallet {
    position: relative;
    width: 1200px;
    height: 778px;
    overflow: hidden;
    background:
      linear-gradient(180deg, rgba(63,111,192,0) 45%, rgba(50,120,200,0.35) 100%),
      linear-gradient(100deg, var(--sky) 0%, var(--mid-blue) 45%, var(--violet) 82%, var(--purple) 100%);
    font-family: "Noto Sans JP", sans-serif;
    color: var(--white);
  }
  .welcome {
    position: absolute;
    right: 62px;
    top: 36px;
    margin: 0;
    font-size: 60px;
    font-weight: 300;
    letter-spacing: 0;
    line-height: 1.2;
  }
  .destinations {
    position: absolute;
    left: 72px;
    top: 138px;
    margin: 0;
    font-size: 49px;
    font-weight: 400;
    letter-spacing: 3px;
    line-height: 1.2;
    white-space: nowrap;
  }
  .photo-row {
    position: absolute;
    top: 242px;
    left: 72px;
    width: 1068px;
    height: 170px;
  }
  .photo {
    position: absolute;
    top: 0;
    width: 170px;
    height: 170px;
    border-radius: 50%;
  }
  .photo--pagoda   { left: 0;     background: linear-gradient(160deg, #8fd0d0 0%, #6aa3a6 45%, #b24a3c 75%, #2f3a34 100%); }
  .photo--castle   { left: 224px; background: linear-gradient(180deg, #a9c9e8 0%, #dfe6ea 45%, #7d8a7a 75%, #3f3a33 100%); }
  .photo--snowtown { left: 449px; background: linear-gradient(180deg, #c8d3e0 0%, #8a8f98 35%, #e8ecf1 65%, #6c6a70 100%); }
  .photo--fuji     { left: 672px; background: linear-gradient(180deg, #1f7fd8 0%, #4aa0e6 40%, #f0b45a 62%, #6d7f98 80%, #3a3a44 100%); }
  .photo--flowers  { left: 898px; background: linear-gradient(180deg, #b7cbe6 0%, #8fb0da 35%, #5a7a44 48%, #e3d925 62%, #c9b710 100%); }
  .scene {
    position: absolute;
    left: 15px;
    top: 443px;
    width: 606px;
    height: 307px;
    background:
      radial-gradient(ellipse 50% 22% at 50% 51%, rgba(var(--silhouette), 0.55) 0%, rgba(var(--silhouette), 0.25) 60%, rgba(var(--silhouette), 0) 100%),
      radial-gradient(ellipse 45% 20% at 50% 72%, rgba(var(--silhouette), 0.18) 0%, rgba(var(--silhouette), 0) 100%);
  }
  .country {
    position: absolute;
    left: 673px;
    top: 462px;
    width: 464px;
    height: 82px;
  }
  .country__rule {
    position: absolute;
    top: 39px;
    width: 77px;
    height: 3px;
    background: var(--cream);
  }
  .country__rule--left  { left: 0; }
  .country__rule--right { right: 0; }
  .country__name {
    position: absolute;
    left: 80px;
    right: 80px;
    top: 0;
    margin: 0;
    text-align: center;
    font-family: "Montserrat", sans-serif;
    font-weight: 600;
    font-size: 84px;
    letter-spacing: 1px;
    line-height: 82px;
    color: var(--cream);
  }
  .partner-name {
    position: absolute;
    left: 945px;
    top: 552px;
    margin: 0;
    font-size: 70px;
    font-weight: 300;
    letter-spacing: 14px;
    line-height: 1.2;
    color: var(--cream);
  }
  .agency {
    position: absolute;
    left: 650px;
    top: 662px;
    width: 478px;
    height: 90px;
    color: var(--ink);
    font-weight: 500;
  }
  .agency__mark {
    position: absolute;
    left: 0;
    top: 9px;
    width: 34px;
    height: 34px;
    border-radius: 50%;
    background: var(--ink);
  }
  .agency__name {
    position: absolute;
    left: 48px;
    top: 0;
    margin: 0;
    font-size: 40px;
    letter-spacing: 2px;
    line-height: 50px;
    white-space: nowrap;
  }
  .agency__tagline {
    position: absolute;
    left: 66px;
    right: 20px;
    top: 46px;
    margin: 0;
    display: flex;
    align-items: center;
    gap: 8px;
    font-size: 28px;
    line-height: 36px;
    letter-spacing: 2px;
  }
  .agency__tagline::before,
  .agency__tagline::after {
    content: "";
    flex: 1;
    height: 2px;
    background: var(--ink);
  }
</style>
</head>
<body>
  <main class="wallet">
    <h1 class="welcome">いらっしゃいませ</h1>
    <p class="destinations">東京・大阪・北海道・九州・北陸・東北・四國</p>

    <div class="photo-row">
      <div class="photo photo--pagoda" role="img" aria-label="Photo of a red pagoda among autumn trees"></div>
      <div class="photo photo--castle" role="img" aria-label="Photo of Osaka Castle against a cloudy sky"></div>
      <div class="photo photo--snowtown" role="img" aria-label="Photo of a snowy Hokkaido town below mountains"></div>
      <div class="photo photo--fuji" role="img" aria-label="Photo of Mount Fuji above a sea of clouds at dawn"></div>
      <div class="photo photo--flowers" role="img" aria-label="Photo of a yellow rapeseed flower field"></div>
    </div>

    <div class="scene" role="img" aria-label="Silhouette illustration of a torii gate and mountains reflected in water, with two birds"></div>

    <div class="country">
      <span class="country__rule country__rule--left"></span>
      <p class="country__name">JAPAN</p>
      <span class="country__rule country__rule--right"></span>
    </div>

    <p class="partner-name">晴空</p>

    <div class="agency">
      <span class="agency__mark"></span>
      <p class="agency__name">SKYBRIDGE TRAVEL</p>
      <p class="agency__tagline">天桥旅行社</p>
    </div>
  </main>
</body>
</html>
```